Homebrew-webshop picture design

I need help with catogory-pics and frontpage-pics for my homebrew-webshop: http://maltkisten.test47.webfjordhost.dk/

My main buiness is raw materials and equipment for small scale beer-brewing.
I would like the pics is welcoming and descriptive.
Cues: Quality products, Customer Care, Personal service,

```html
<!DOCTYPE html>
<html lang="da">
<head>
<meta charset="utf-8">
<title>Maltkisten.dk – Hjem</title>
<link rel="stylesheet" href="https://fonts.googleapis.com/css2?family=Source+Sans+3:wght@400;600;700&display=swap">
<style>
:root{
  --teal:#3fb0a6;
  --dark:#474747;
  --footer:#4b4b4b;
  --page:#f4f4f4;
  --text:#333;
  --muted:#555;
  --white:#fff;
  --blue:#2f7bbf;
}
*{box-sizing:border-box;margin:0;padding:0}
html,body{width:1200px;height:2583px;overflow:hidden}
body{font-family:"Source Sans 3",sans-serif;color:var(--text);background:var(--page);position:relative}
.wrap{position:absolute;left:100px;width:1000px}
.usp-bar{position:absolute;top:0;left:0;width:1200px;height:21px;background:var(--teal);color:var(--white);font-size:13px}
.usp-bar span{position:absolute;top:2px;display:flex;align-items:center;gap:4px}
.site-header{position:absolute;top:21px;left:0;width:1200px;height:83px;background:#f7f7f7}
.logo{position:absolute;left:100px;top:18px;font-size:40px;color:var(--blue);font-weight:400}
.search{position:absolute;left:391px;top:23px;width:416px;height:38px;border:1px solid #999;background:var(--white);font-size:14px;color:#555;padding:9px 16px}
.search svg{position:absolute;right:14px;top:9px}
.header-links{position:absolute;top:20px;font-size:14px;text-align:center;color:#222}
.header-links svg{display:block;margin:0 auto 2px}
.badge{position:absolute;top:-7px;right:-14px;width:17px;height:17px;border-radius:50%;background:#111;color:#fff;font-size:11px;line-height:17px}
.main-nav{position:absolute;top:104px;left:0;width:1200px;height:42px;background:var(--dark);color:var(--white);font-size:13px;font-weight:600}
.main-nav span{position:absolute;top:13px}
.hero{position:absolute;top:146px;left:0;width:1200px;height:449px;background:linear-gradient(90deg,#4a4744 0%,#5a5550 35%,#8a6a3a 55%,#b58a45 70%,#6b5a45 100%)}
.hero-inner{position:absolute;left:100px;top:95px;color:var(--white)}
.hero-title{font-size:48px;font-weight:400;margin-bottom:30px}
.hero-text{font-size:20px;font-weight:600;line-height:30px;width:350px}
.btn{display:inline-block;background:var(--teal);color:var(--white);font-weight:600;border-radius:2px;text-align:center}
.hero .btn{margin-top:38px;width:99px;height:33px;line-height:33px;font-size:18px}
.welcome-title{position:absolute;top:655px;left:0;width:1200px;text-align:center;font-size:24px;font-weight:600;color:#333}
.welcome-text{top:713px;font-size:13px;line-height:20px;color:var(--muted)}
.tile{position:absolute;height:233px;color:var(--white);font-size:28px;font-weight:600;letter-spacing:2px}
.tile span{position:absolute;left:17px;bottom:18px}
.section-title{position:absolute;top:1603px;left:100px;font-size:24px;font-weight:600}
.product{position:absolute;top:1675px;width:221px;height:408px;background:var(--white);text-align:center}
.product .photo{position:absolute;left:20px;top:20px;width:181px;height:240px}
.product .name{position:absolute;top:276px;left:10px;right:10px;font-size:16px;color:#444;line-height:21px}
.product .from{position:absolute;top:313px;width:100%;font-size:11px;color:#666}
.product .price{position:absolute;top:329px;width:100%;font-size:14px;font-weight:600}
.product .btn{position:absolute;top:353px;left:61px;width:100px;height:32px;line-height:32px;font-size:16px}
.newsletter{position:absolute;top:2140px;left:0;width:1200px;height:70px;background:var(--white)}
.newsletter .label{position:absolute;left:286px;top:28px;font-size:12px}
.newsletter .field{position:absolute;left:491px;top:17px;width:323px;height:33px;border:1px solid #ccc;font-size:12px;color:#777;padding:9px 8px}
.newsletter .btn{position:absolute;left:823px;top:17px;width:92px;height:33px;line-height:33px;font-size:17px}
.site-footer{position:absolute;top:2210px;left:0;width:1200px;height:301px;background:var(--footer);color:var(--white)}
.col{position:absolute;top:37px}
.col h3{font-size:20px;font-weight:600;margin-bottom:17px}
.col li{list-style:none;font-size:15px;height:31px;display:flex;align-items:center;gap:8px}
.col.links li{height:38px}
.social li{height:38px}
.dot{width:22px;height:22px;border-radius:50%;background:#eee;display:inline-block}
.bottom{position:absolute;top:2511px;left:0;width:1200px;height:72px;background:var(--white);text-align:center}
.cards{position:absolute;left:478px;top:6px;width:248px;height:34px;border:1px solid #ddd;display:flex;gap:6px;justify-content:center;align-items:center}
.cards i{display:block;width:32px;height:20px;border-radius:3px;background:#d9dee6}
.copyright{position:absolute;top:48px;width:100%;font-size:11px;font-weight:600}
</style>
</head>
<body>

<div class="usp-bar">
  <span style="left:100px"><svg width="12" height="12" viewBox="0 0 12 12"><rect x="1" y="1" width="10" height="10" fill="none" stroke="#fff"/><path d="M3 6l2 2 4-5" fill="none" stroke="#fff" stroke-width="1.5"/></svg>Fragt kun DKK 35,-</span>
  <span style="left:378px"><svg width="12" height="12" viewBox="0 0 12 12"><rect x="1" y="1" width="10" height="10" fill="none" stroke="#fff"/><path d="M3 6l2 2 4-5" fill="none" stroke="#fff" stroke-width="1.5"/></svg>Fri fragt ved Køb over 500,-</span>
  <span style="left:701px"><svg width="12" height="12" viewBox="0 0 12 12"><rect x="1" y="1" width="10" height="10" fill="none" stroke="#fff"/><path d="M3 6l2 2 4-5" fill="none" stroke="#fff" stroke-width="1.5"/></svg>Sikker betaling</span>
  <span style="left:989px"><svg width="12" height="12" viewBox="0 0 12 12"><rect x="1" y="1" width="10" height="10" fill="none" stroke="#fff"/><path d="M3 6l2 2 4-5" fill="none" stroke="#fff" stroke-width="1.5"/></svg>30 dages returret</span>
</div>

<header class="site-header">
  <div class="logo">Maltkisten.dk</div>
  <div class="search">Indtast søgeord…
    <svg width="18" height="18" viewBox="0 0 18 18"><circle cx="7.5" cy="7.5" r="6" fill="none" stroke="#333" stroke-width="1.6"/><path d="M12 12l5 5" stroke="#333" stroke-width="1.6"/></svg>
  </div>
  <div class="header-links" style="left:921px">
    <svg width="20" height="20" viewBox="0 0 20 20"><rect x="3" y="9" width="14" height="10" rx="1" fill="none" stroke="#222" stroke-width="1.5"/><path d="M6 9V6a4 4 0 0 1 8 0v3" fill="none" stroke="#222" stroke-width="1.5"/></svg>Login</div>
  <div class="header-links" style="left:978px">
    <svg width="26" height="20" viewBox="0 0 26 20"><circle cx="10" cy="6" r="4" fill="none" stroke="#222" stroke-width="1.5"/><path d="M2 19c0-5 4-7 8-7s8 2 8 7z" fill="none" stroke="#222" stroke-width="1.5"/><path d="M21 5v6M18 8h6" stroke="#222" stroke-width="1.5"/></svg>Bliv kunde</div>
  <div class="header-links" style="left:1062px">
    <div style="position:relative;width:24px;margin:0 auto"><svg width="20" height="20" viewBox="0 0 20 20"><rect x="3" y="6" width="14" height="13" fill="none" stroke="#222" stroke-width="1.5"/><path d="M7 8V4a3 3 0 0 1 6 0v4" fill="none" stroke="#222" stroke-width="1.5"/></svg><span class="badge">0</span></div>Kurv</div>
</header>

<nav class="main-nav">
  <span style="left:100px;top:11px"><svg width="17" height="17" viewBox="0 0 17 17"><path d="M2 8l6.5-6 6.5 6M4 7v8h9V7" fill="none" stroke="#fff" stroke-width="1.3"/></svg></span>
  <span style="left:140px">RÅVARER ⌄</span>
  <span style="left:222px">BRYGNING OG GÆRING ⌄</span>
  <span style="left:382px">TAPNING ⌄</span>
  <span style="left:463px">RENGØRING ⌄</span>
  <span style="left:563px">LABORATORIET</span>
  <span style="left:679px">SNAPS ⌄</span>
  <span style="left:747px">BØGER</span>
</nav>

<section class="hero" role="img" aria-label="Foto af et glas øl med skum, byg-aks og friske humlekopper på et mørkt træbord">
  <div class="hero-inner">
    <div class="hero-title">Maltkisten</div>
    <p class="hero-text">Lorem ipsum dolor sit amet, consetetur sadipscing elitr, sed diam nonumy eirmod tempor invidunt ut labore et.</p>
    <span class="btn">Køb nu</span>
  </div>
</section>

<h2 class="welcome-title">VELKOMMEN TIL MALTKISTEN</h2>
<p class="wrap welcome-text">Lorem ipsum dolor sit amet, consectetur adipiscing elit. Proin semper turpis eu lacus consectetur, ut pharetra augue dignissim. Suspendisse condimentum pulvinar nibh, eu vestibulum lorem pellentesque a. Cras at auctor urna. Pellentesque luctus ultricies nibh eu egestas. Vestibulum fringilla libero sem, a fermentum magna ultrices sed. Sed lectus nibh, facilisis nec scelerisque sed, varius vulputate ipsum. Phasellus velit dui, rhoncus in placerat nec, rhoncus sed ligula. Aenean pharetra porta ullamcorper.</p>

<a class="tile" style="left:100px;top:815px;width:491px;background:linear-gradient(120deg,#6e5f4c,#8c7a62 50%,#5b4a38)" role="img" aria-label="Foto af en sæk maltkorn med træske"><span>RÅVARER</span></a>
<a class="tile" style="left:608px;top:815px;width:491px;background:linear-gradient(120deg,#9a5a35,#b98a55 40%,#c9cccc 75%,#8f9696)" role="img" aria-label="Foto af tappehaner på et bryganlæg"><span>BRYGNING OG GÆRING</span></a>
<a class="tile" style="left:100px;top:1065px;width:322px;background:linear-gradient(120deg,#6b4a30,#8a6142 60%,#4a5a30)" role="img" aria-label="Foto af grønne ølflasker og korn på træbord"><span>TAPNING</span></a>
<a class="tile" style="left:439px;top:1065px;width:322px;background:linear-gradient(120deg,#7a4a2c,#b08a5a 50%,#5a3a22)" role="img" aria-label="Foto af skuresbørster på et træbord"><span>RENGØRING</span></a>
<a class="tile" style="left:778px;top:1065px;width:322px;background:linear-gradient(120deg,#6e6e6a,#c9b98a 50%,#d8d0c8)" role="img" aria-label="Foto af laboratorieglas med gul væske"><span>LABORATORIET</span></a>
<a class="tile" style="left:100px;top:1315px;width:491px;background:linear-gradient(120deg,#5a4632,#7d6444 45%,#b08d62)" role="img" aria-label="Foto af en flaske snaps på brunt papir"><span>SNAPS</span></a>
<a class="tile" style="left:608px;top:1315px;width:491px;background:linear-gradient(120deg,#4a3a2c,#6b5540 45%,#c9a880 80%,#e8d0a0)" role="img" aria-label="Foto af en stak bøger"><span>BØGER</span></a>

<h2 class="section-title">NYESTE PRODUKTER</h2>

<article class="product" style="left:100px">
  <div class="photo" role="img" aria-label="Produktfoto af en pose malt med humle og gær" style="background:radial-gradient(ellipse at 45% 50%,#b59a72 0%,#d8c8ae 45%,#fff 72%)"></div>
  <div class="name">Bland selv opskrift</div>
  <div class="from">Priser fra</div>
  <div class="price">0,03 kr</div>
  <span class="btn">Tilføj kurv</span>
</article>
<article class="product" style="left:357px">
  <div class="photo" role="img" aria-label="Produktfoto af en 5 liters glasdunk" style="background:radial-gradient(ellipse at 50% 55%,#e4eae8 0%,#f2f5f4 45%,#fff 70%)"></div>
  <div class="name">Demijohn 5 liter</div>
  <div class="price">54,95 kr</div>
  <span class="btn">Tilføj kurv</span>
</article>
<article class="product" style="left:614px">
  <div class="photo" role="img" aria-label="Produktfoto af en vandvarmer i rustfrit stål" style="background:radial-gradient(ellipse at 50% 50%,#8a8a8a 0%,#c8c8c8 40%,#fff 66%)"></div>
  <div class="name">Maltmester Sparge Water Heater 18 liter</div>
  <div class="price">849,00 kr</div>
  <span class="btn">Tilføj kurv</span>
</article>
<article class="product" style="left:878px">
  <div class="photo" role="img" aria-label="Produktfoto af et rødt roterende flasketræ med grønne flasker" style="background:radial-gradient(ellipse at 50% 50%,#c83a34 0%,#6a8a4a 35%,#fff 66%)"></div>
  <div class="name">Flasketræ - Roterende</div>
  <div class="price">298,00 kr</div>
  <span class="btn">Tilføj kurv</span>
</article>

<section class="newsletter">
  <span class="label">TILMELD DIG VORES NYHEDSBREV</span>
  <div class="field">Indtast din e-mailadresse</div>
  <span class="btn">Tilmeld</span>
</section>

<footer class="site-footer">
  <div class="col" style="left:100px">
    <h3>KONTAKT</h3>
    <ul>
      <li>Maltkisten</li>
      <li>Humlevej 14</li>
      <li>8000 Byhavn</li>
      <li>CVR DK00000000</li>
      <li><svg width="24" height="22" viewBox="0 0 24 22"><rect x="2" y="1" width="20" height="20" rx="2" fill="#eee"/><path d="M8 6c0 5 4 9 9 9l1-2-3-1-1 1c-2-1-3-2-4-4l1-1-1-3z" fill="#4b4b4b"/></svg>12 34 56 78</li>
      <li><svg width="26" height="20" viewBox="0 0 26 20"><rect x="1" y="3" width="24" height="15" fill="#eee"/><path d="M1 3l12 9 12-9" fill="none" stroke="#4b4b4b" stroke-width="1.5"/></svg>info@maltkisten.dk</li>
    </ul>
  </div>
  <div class="col links" style="left:393px">
    <h3>KUNDESERVICE</h3>
    <ul><li>Ofte stillede spørgsmål</li><li>Handelsvilkår</li><li>Privatlivspolitik</li><li>Her finder du os</li><li>Kontakt os</li></ul>
  </div>
  <div class="col links" style="left:687px">
    <h3>INFORMATION</h3>
    <ul><li>Information</li><li>Om os</li><li>Sådan handler du</li><li>Sikker handel</li><li>Vejledning</li></ul>
  </div>
  <div class="col social" style="left:980px">
    <h3>VI ER SOCIALE</h3>
    <ul>
      <li><span class="dot"></span>Bryggerbog</li>
      <li><span class="dot"></span>Billedvæg</li>
      <li><span class="dot"></span>Kvidder</li>
      <li><span class="dot"></span>Søgeplus</li>
      <li><span class="dot"></span>Filmkanal</li>
    </ul>
  </div>
</footer>

<div class="bottom">
  <div class="cards" aria-label="Betalingsmuligheder"><i></i><i></i><i></i><i></i><i></i><i></i></div>
  <div class="copyright">Copyright © 2020 Maltkisten. All rights reserved.</div>
</div>

</body>
</html>
```